Norvane Builders Business Card

Modern and Professional Business Card for a Med size construction/development company.

See the samples below for the design I like … but I need ideas for incorporating the red company logo while still keeping the clean look of the card samples that are attached.

Logo and tag line on the back … info on the front.

Tagline: Quality Starts from the Ground Up

Target Market(s)

Med-Large General Contractors

Contact Information for Business Card

Norvane Builders Limited
42 Brenton Street
Elk Harbour, NL
B3K 7T2

t: 709-555-0147
f: 709-555-0192
w: www.norvanebuilders-example.com

Font styles to use
Sans Serif

Colors
fbee3e

Requirements
Must have
• I like the black and yellow designs of the attached samples …. but I'm not sure how to incorporate the red Norvane Builders logo into that design??
Nice to have
• Construction safety strips

```html
<!DOCTYPE html>
<html lang="en">
<head>
<meta charset="UTF-8">
<title>Norvane Builders Business Card</title>
<link href="https://fonts.googleapis.com/css2?family=Lato:wght@400;700;900&display=swap" rel="stylesheet">
<style>
  :root {
    --brand-red: #e8232f;
    --brand-red-dark: #d81e2a;
    --ink: #2b2b2b;
    --paper: #ffffff;
    --rule: #c9c9c9;
    --stage: #3a3a3a;
  }
  * { box-sizing: border-box; margin: 0; padding: 0; }
  html, body {
    width: 1200px; height: 1015px; overflow: hidden;
    background: var(--stage);
    font-family: "Lato", sans-serif;
  }
  .card {
    position: absolute; left: 220px;
    width: 760px; height: 434px;
    box-shadow: 0 12px 30px rgba(0,0,0,.45);
    overflow: hidden;
  }
  /* Back side */
  .card-back { top: 48px; }
  .card-back .pattern-field {
    position: absolute; inset: 0;
    background: linear-gradient(135deg, var(--brand-red) 0%, var(--brand-red-dark) 100%);
  }
  .back-mark {
    position: absolute; right: 46px; top: 118px;
    display: flex; align-items: center; gap: 8px;
    color: var(--paper); font-weight: 900; font-size: 17px; letter-spacing: .5px;
  }
  .back-mark .mark-square { width: 12px; height: 12px; background: var(--paper); }
  .tagline {
    position: absolute; left: 0; right: 0; bottom: 92px;
    text-align: center; color: var(--paper);
    font-size: 14px; font-weight: 400; letter-spacing: 1.4px; text-transform: uppercase;
  }
  /* Front side */
  .card-front { top: 530px; background: var(--paper); }
  .front-band {
    position: absolute; left: 0; right: 0; bottom: 0; height: 18px;
    background: var(--brand-red);
  }
  .front-mark {
    position: absolute; left: 60px; top: 190px; width: 270px;
    display: flex; align-items: center; gap: 10px;
    color: var(--brand-red); font-weight: 900; font-size: 27px; letter-spacing: .5px;
  }
  .front-mark .mark-square { width: 18px; height: 18px; background: var(--brand-red); flex: none; }
  .divider {
    position: absolute; left: 370px; top: 95px; width: 1px; height: 215px;
    background: var(--rule);
  }
  .contact {
    position: absolute; left: 400px; top: 98px;
    color: var(--ink); font-size: 17px; line-height: 1.22;
  }
  .contact .person-name { color: var(--brand-red); font-weight: 900; font-size: 22px; letter-spacing: .3px; }
  .contact .person-title { margin-bottom: 4px; }
  .contact .line { display: flex; align-items: center; gap: 7px; }
  .contact .line svg { width: 14px; height: 14px; fill: var(--brand-red); flex: none; }
  .contact .company { color: var(--brand-red); margin-top: 4px; }
</style>
</head>
<body>
  <section class="card card-back" aria-label="Card back">
    <div class="pattern-field" role="img" aria-label="Tiled repeat of the company mark in slightly lighter red"></div>
    <div class="back-mark"><span class="mark-square"></span>NORVANE BUILDERS</div>
    <p class="tagline">Quality Starts From The Ground Up</p>
  </section>

  <section class="card card-front" aria-label="Card front">
    <div class="front-mark"><span class="mark-square"></span>NORVANE BUILDERS</div>
    <div class="divider"></div>
    <div class="contact">
      <div class="person-name">DANIEL HARTLEY</div>
      <div class="person-title">Managing Director</div>
      <div class="line">
        <svg viewBox="0 0 24 24" aria-hidden="true"><path d="M6.6 10.8a15.1 15.1 0 0 0 6.6 6.6l2.2-2.2a1 1 0 0 1 1-.25 11.4 11.4 0 0 0 3.6.57 1 1 0 0 1 1 1V20a1 1 0 0 1-1 1A17 17 0 0 1 3 4a1 1 0 0 1 1-1h3.5a1 1 0 0 1 1 1c0 1.25.2 2.45.57 3.57a1 1 0 0 1-.25 1z"/></svg>
        709-555-0147
      </div>
      <div class="line">
        <svg viewBox="0 0 24 24" aria-hidden="true"><path d="M6 3h12v5H6zM4 9h16a2 2 0 0 1 2 2v6h-4v4H6v-4H2v-6a2 2 0 0 1 2-2zm4 7v3h8v-3z"/></svg>
        709-555-0192
      </div>
      <div class="line">
        <svg viewBox="0 0 24 24" aria-hidden="true"><circle cx="12" cy="12" r="10"/></svg>
        www.norvanebuilders-example.com
      </div>
      <div class="company">Norvane Builders Limited</div>
      <div>42 Brenton Street</div>
      <div>Elk Harbour, NL B3K 7T2</div>
    </div>
    <div class="front-band"></div>
  </section>
</body>
</html>
```